Criação de Cartao de Visita para Computador & Internet
" Nossos clientes fazem o outsorcing da TI para nós, assim cuidamos de todos os recursos se serviços de TI, também vendemos hardwares e softwares "

```html
<!DOCTYPE html>
<html lang="pt-BR">
<head>
<meta charset="utf-8">
<title>Cartão de Visita – Nuvix Corp</title>
<link rel="stylesheet" href="https://fonts.googleapis.com/css2?family=Roboto:wght@400;500;700&display=swap">
<style>
  :root{
    --page:#ffffff;
    --navy:#0b3a5e;
    --blue:#1f6fa8;
    --ink:#23507a;
    --white:#ffffff;
  }
  *{box-sizing:border-box;margin:0;padding:0}
  html,body{width:1200px;height:1200px;overflow:hidden;background:var(--page)}
  body{font-family:"Roboto",Arial,sans-serif;position:relative}
  .card{position:absolute;left:149px;width:895px;height:485px;overflow:hidden;
        box-shadow:0 8px 18px rgba(0,0,0,.22)}
  .card-front{top:96px;border-radius:18px 90px 18px 90px}
  .card-back{top:624px;border-radius:90px 18px 90px 18px;background:linear-gradient(180deg,#fafbfc,#e7eaed)}
  .card svg.bg{position:absolute;inset:0}
  .brand{position:absolute;left:60px;top:200px;width:330px;text-align:center;color:var(--blue);
         font-weight:700;font-size:52px;line-height:1.1}
  .person{position:absolute;left:520px;top:92px;color:var(--white)}
  .person-name{font-size:34px;font-weight:500}
  .person-role{font-size:19px;font-weight:700;margin-top:4px}
  .person-division{font-size:16px;font-weight:700;margin-top:16px;letter-spacing:.5px}
  .contacts{position:absolute;left:520px;top:212px;list-style:none;color:var(--white);font-size:16px}
  .contacts li{display:flex;align-items:center;gap:14px;margin-bottom:12px;line-height:1.25}
  .contacts svg{flex:none;width:28px;height:28px}
  .col{position:absolute;top:44px}
  .col-ti{left:40px;width:370px}
  .col-eventos{left:465px;width:370px}
  .col-title{text-align:center;font-size:24px;font-weight:700;color:var(--navy)}
  .col-sub{text-align:center;font-size:17px;font-weight:700;color:var(--blue);margin-top:8px;line-height:1.2}
  .services{list-style:none;margin-top:34px;color:var(--ink);font-size:17px}
  .services li{position:relative;padding-left:20px;margin-bottom:14px;line-height:1.2}
  .services li::before{content:"";position:absolute;left:2px;top:7px;width:7px;height:7px;border-radius:50%;background:var(--blue)}
  .col-ti .services{padding-left:16px;max-width:330px}
  .col-eventos .services{padding-left:12px}
  .col-eventos .services li{margin-bottom:11px}
  .divider{position:absolute;left:438px;top:50px;width:3px;height:330px;background:var(--blue)}
</style>
</head>
<body>

<section class="card card-front">
  <svg class="bg" width="895" height="485" viewBox="0 0 895 485" aria-hidden="true">
    <defs>
      <linearGradient id="frontBlue" x1="0" y1="0" x2="1" y2="1">
        <stop offset="0" stop-color="#0e4f80"/>
        <stop offset="1" stop-color="#2f8fcb"/>
      </linearGradient>
      <linearGradient id="frontLight" x1="0" y1="0" x2="0" y2="1">
        <stop offset="0" stop-color="#ffffff"/>
        <stop offset="1" stop-color="#dfe3e7"/>
      </linearGradient>
    </defs>
    <rect width="895" height="485" fill="url(#frontBlue)"/>
    <circle cx="780" cy="420" r="260" fill="#ffffff" opacity=".06"/>
    <rect x="0" y="0" width="200" height="485" fill="url(#frontLight)"/>
    <circle cx="225" cy="255" r="250" fill="url(#frontLight)"/>
  </svg>
  <div class="brand">Nuvix<br>Corp</div>
  <div class="person">
    <div class="person-name">Marina Coutinho</div>
    <div class="person-role">Diretora Executiva</div>
    <div class="person-division">DIVISÃO DE EVENTOS</div>
  </div>
  <ul class="contacts">
    <li>
      <svg viewBox="0 0 28 28" aria-hidden="true"><circle cx="14" cy="14" r="13" fill="#ffffff" opacity=".3"/><path d="M10 8l3 3-2 2a9 9 0 004 4l2-2 3 3-2 2c-5 0-10-5-10-10z" fill="#fff"/></svg>
      <span>11 3456-7890 (São Paulo)<br>0800 123 4567 (Demais localidades)</span>
    </li>
    <li>
      <svg viewBox="0 0 28 28" aria-hidden="true"><circle cx="14" cy="14" r="13" fill="#ffffff" opacity=".3"/><rect x="10" y="7" width="8" height="14" rx="1.5" fill="none" stroke="#fff" stroke-width="1.6"/><circle cx="14" cy="18.5" r="0.9" fill="#fff"/></svg>
      <span>11 91234-5678</span>
    </li>
    <li>
      <svg viewBox="0 0 28 28" aria-hidden="true"><circle cx="14" cy="14" r="13" fill="#ffffff" opacity=".3"/><rect x="8" y="9" width="12" height="10" rx="1" fill="none" stroke="#fff" stroke-width="1.6"/><path d="M8 10l6 5 6-5" fill="none" stroke="#fff" stroke-width="1.6"/></svg>
      <span>contato@nuvixcorp.com.br</span>
    </li>
    <li>
      <svg viewBox="0 0 28 28" aria-hidden="true"><circle cx="14" cy="14" r="13" fill="#ffffff" opacity=".3"/><circle cx="14" cy="14" r="6.5" fill="none" stroke="#fff" stroke-width="1.5"/><path d="M7.5 14h13M14 7.5c-3 3.5-3 9.5 0 13M14 7.5c3 3.5 3 9.5 0 13" fill="none" stroke="#fff" stroke-width="1.2"/></svg>
      <span>www.nuvixcorp.com.br</span>
    </li>
  </ul>
</section>

<section class="card card-back">
  <svg class="bg" width="895" height="485" viewBox="0 0 895 485" aria-hidden="true">
    <circle cx="645" cy="235" r="232" fill="#ffffff" stroke="#d7dce1" stroke-width="3"/>
    <path d="M0 410 Q300 470 620 485 L0 485 Z" fill="#d7dce1" opacity=".6"/>
  </svg>
  <div class="col col-ti">
    <h2 class="col-title">Divisão de TI</h2>
    <p class="col-sub">Soluções em Tecnologia<br>da Informação</p>
    <ul class="services">
      <li>Administração e Suporte de TI (outsourcing)</li>
      <li>Cloud Solutions - Nuvem Corporativa</li>
      <li>Cotação e Venda de Hardware e Software</li>
      <li>Consultoria e Projetos de TI</li>
      <li>Segurança e Proteção de Dados</li>
    </ul>
  </div>
  <div class="divider"></div>
  <div class="col col-eventos">
    <h2 class="col-title">Divisão de Eventos</h2>
    <p class="col-sub">Informação, Gestão e Negócio<br>para o Segmento Jurídico</p>
    <ul class="services">
      <li>Seminários</li>
      <li>Congressos</li>
      <li>Comitês</li>
      <li>Cursos</li>
      <li>Workshop</li>
      <li>Networking</li>
      <li>Conexões Empresariais</li>
    </ul>
  </div>
</section>

</body>
</html>
```